Window and GutterCleaning Flyer A5 size double sided.

We need a double sided A5 flyer. Side 1, is for window cleaning, side 2 is for gutter cleaning. Licensed by Borough of Halvern Council.
Phone number 0800 315 4720.
Business address 7 Tarnlow Brae, North Pellin Edinburgh EH14 3RW.
www.clearpane-vista-services.com
We use a LoftPro Gutter inspection Cam to view your gutters first to see if they need doing.
Window cleaning ; Professional window cleaning services, what we offer, water fed pole window cleaning able to reach windows up to 60 feet.
Conservatory cleaning.
Conservatory roof cleaning.
Fascias & Soffits cleaning.
Excellent Customer Service.
Target Market(s)
domestic houses
Industry/Entity Type
window cleaning
Look and feel
Each slider illustrates characteristics of the customer's brand and the style your logo design should communicate.

```html
<!DOCTYPE html>
<html lang="en">
<head>
<meta charset="utf-8">
<title>ClearPane Vista – Window &amp; Gutter Cleaning Flyer</title>
<link href="https://fonts.googleapis.com/css2?family=Oswald:wght@500;600&family=Roboto:wght@400;500;700;900&display=swap" rel="stylesheet">
<style>
  :root{
    --navy:#24215f;
    --navy-deep:#1d1a52;
    --sky:#4f97d6;
    --sky-light:#9cc7ec;
    --paper:#eef2f6;
    --paper-blue:#d7e6f1;
    --ink:#2b2b3a;
    --mat:#a3a3a3;
    --white:#ffffff;
  }
  *{margin:0;padding:0;box-sizing:border-box}
  html,body{width:1200px;height:826px;overflow:hidden;background:var(--mat)}
  body{position:relative;font-family:"Roboto",Arial,sans-serif;color:var(--ink)}
  .flyer{position:absolute;top:35px;width:528px;height:750px;overflow:hidden;background:var(--paper)}
  .flyer--window{left:54px}
  .flyer--gutter{left:623px}
  .flyer-shapes{position:absolute;inset:0;width:528px;height:750px}
  .abs{position:absolute}
  .headline{font-family:"Oswald",Impact,sans-serif;font-weight:600;line-height:.92;letter-spacing:-.5px;text-transform:uppercase}
  .headline .lg{color:var(--white)}
  .headline .md{color:var(--sky-light)}
  .brand{display:flex;align-items:center;gap:6px;font-family:"Roboto",Arial,sans-serif;font-weight:900;font-size:17px;color:var(--navy);white-space:nowrap}
  .brand .dot{width:12px;height:12px;background:var(--navy)}
  .offer-title{font-family:"Roboto",Arial,sans-serif;font-weight:900;font-size:28px;color:var(--white);letter-spacing:-.5px}
  .offer-list{list-style:none}
  .offer-list li{display:flex;align-items:center;gap:8px;font-weight:500;font-size:17px;color:var(--ink);height:33.5px;position:relative}
  .offer-list li + li::before{content:"";position:absolute;left:24px;top:-1px;width:225px;border-top:1px solid var(--sky)}
  .tick{width:18px;height:18px;flex:none}
  .reach{width:200px;text-align:center;color:var(--navy);font-size:14px;line-height:1.1}
  .pill{display:inline-block;margin-top:6px;background:var(--navy);color:var(--white);font-weight:700;font-size:14px;padding:3px 9px;border-radius:11px}
  .cam-note{font-size:14px;line-height:1.17;color:var(--ink);width:196px}
  .contact{color:var(--white)}
  .contact .addr{font-size:11.5px}
  .contact .phone{display:flex;align-items:center;gap:4px;font-weight:700;font-size:25px;line-height:1.1;margin-top:3px}
  .contact .phone svg{width:15px;height:18px}
  .contact .web{font-weight:500;font-size:14px;color:var(--sky-light);margin-top:1px}
  .intro{font-weight:700;font-size:16px;line-height:1.03;color:var(--navy);width:210px}
  .body-copy{font-size:11px;line-height:1.12;color:#3a3a48}
  .body-copy p + p{margin-top:11px}
  .card{position:absolute;width:117px;height:157px;border-radius:9px;background:var(--sky);overflow:hidden;border:2px solid var(--white)}
  .card .photo{height:118px;border-radius:0 0 9px 9px}
  .card .label{color:var(--white);font-weight:700;font-size:10.5px;line-height:1.05;padding:6px 0 0 14px}
</style>
</head>
<body>

<section class="flyer flyer--window" aria-label="Window cleaning flyer">
  <svg class="flyer-shapes" viewBox="0 0 528 750">
    <rect width="528" height="750" fill="var(--paper)"/>
    <rect width="528" height="150" fill="var(--paper-blue)"/>
    <polygon points="370,0 528,0 528,80" fill="var(--white)"/>
    <polygon points="222,88 395,0 528,70 528,300 355,370 222,285" fill="var(--white)"/>
    <polygon role="img" aria-label="Photo: a cleaner wiping a window with a squeegee" points="229,98 393,6 528,80 528,292 356,362 229,281" fill="url(#heroGrad)"/>
    <polygon points="0,150 218,150 218,285 258,309 0,309" fill="var(--navy)"/>
    <polygon points="0,317 303,317 343,360 0,360" fill="var(--sky)"/>
    <rect x="28" y="522" width="488" height="100" rx="10" fill="#e2e6ea"/>
    <polygon role="img" aria-label="Photo: gutter inspection camera with monitor" points="366,462 505,462 505,622 402,622 402,550 366,550" fill="url(#camGrad)"/>
    <polygon points="0,638 528,638 528,750 0,750" fill="var(--sky-light)"/>
    <polygon points="210,646 528,646 528,750 210,750" fill="var(--navy)"/>
    <polygon points="0,585 50,548 210,640 210,750 0,750" fill="var(--navy)"/>
    <polygon role="img" aria-label="Photo: brick house with a white conservatory" points="0,596 50,560 204,648 204,750 0,750" fill="url(#houseGrad)"/>
    <defs>
      <linearGradient id="heroGrad" x1="0" y1="0" x2="1" y2="1">
        <stop offset="0" stop-color="#8f9a8a"/><stop offset=".5" stop-color="#c8cfcc"/><stop offset="1" stop-color="#a88f6e"/>
      </linearGradient>
      <linearGradient id="camGrad" x1="0" y1="0" x2="0" y2="1">
        <stop offset="0" stop-color="#4a5a6a"/><stop offset="1" stop-color="#2a2a2e"/>
      </linearGradient>
      <linearGradient id="houseGrad" x1="0" y1="0" x2="0" y2="1">
        <stop offset="0" stop-color="#c9d8e6"/><stop offset=".6" stop-color="#b86a4e"/><stop offset="1" stop-color="#7c9b52"/>
      </linearGradient>
    </defs>
  </svg>

  <div class="abs brand" style="left:30px;top:68px"><span class="dot"></span>ClearPane Vista</div>

  <h1 class="abs headline" style="left:22px;top:170px;width:190px">
    <span class="lg" style="display:block;font-size:30px;line-height:1">Professional</span>
    <span class="md" style="display:block;font-size:24px;line-height:1">Window Cleaning</span>
    <span class="lg" style="display:block;font-size:50px;line-height:1">Services</span>
  </h1>

  <h2 class="abs offer-title" style="left:25px;top:320px">WHAT WE OFFER</h2>

  <ul class="abs offer-list" style="left:26px;top:371px">
    <li><svg class="tick" viewBox="0 0 20 20"><circle cx="10" cy="10" r="9" fill="var(--sky)"/><path d="M5.5 10.5l3 3 6-6.5" stroke="#fff" stroke-width="2.2" fill="none"/></svg>Conservatory cleaning</li>
    <li><svg class="tick" viewBox="0 0 20 20"><circle cx="10" cy="10" r="9" fill="var(--sky)"/><path d="M5.5 10.5l3 3 6-6.5" stroke="#fff" stroke-width="2.2" fill="none"/></svg>Conservatory roof cleaning</li>
    <li><svg class="tick" viewBox="0 0 20 20"><circle cx="10" cy="10" r="9" fill="var(--sky)"/><path d="M5.5 10.5l3 3 6-6.5" stroke="#fff" stroke-width="2.2" fill="none"/></svg>Fascias &amp; Soffits cleaning</li>
    <li><svg class="tick" viewBox="0 0 20 20"><circle cx="10" cy="10" r="9" fill="var(--sky)"/><path d="M5.5 10.5l3 3 6-6.5" stroke="#fff" stroke-width="2.2" fill="none"/></svg>Excellent Customer Service</li>
  </ul>

  <div class="abs reach" style="left:313px;top:387px">Water fed pole<br>window cleaning able to reach<br><span class="pill">Windows up to 60 feet</span></div>

  <p class="abs cam-note" style="left:194px;top:538px">We use a LoftPro Gutter<br>inspection Cam to<br>view your gutters first to see<br>if they need doing.</p>

  <div class="abs contact" style="left:238px;top:670px">
    <div class="addr">7 Tarnlow Brae, North Pellin Edinburgh EH14 3RW</div>
    <div class="phone"><svg viewBox="0 0 16 20"><path d="M4 1l3 4-2 2c1 3 3 6 5 7l2-2 3 3-2 3C6 17 1 9 2 3z" fill="var(--sky-light)"/></svg>0800 315 4720</div>
    <div class="web">www.clearpane-vista-services.com</div>
  </div>
</section>

<section class="flyer flyer--gutter" aria-label="Gutter cleaning flyer">
  <svg class="flyer-shapes" viewBox="0 0 528 750">
    <rect width="528" height="750" fill="var(--paper)"/>
    <rect width="528" height="99" fill="var(--navy)"/>
    <polygon points="0,72 77,32 200,99 0,99" fill="var(--paper)"/>
    <polygon points="200,104 528,104 528,148 270,148" fill="var(--sky)"/>
    <polygon points="0,80 77,38 240,132 240,330 0,330" fill="var(--white)"/>
    <polygon role="img" aria-label="Photo: gloved hand pulling autumn leaves from a gutter" points="0,86 77,44 236,136 236,320 148,270 0,330" fill="url(#leafGrad)"/>
    <polygon points="0,323 148,246 270,318 270,400 0,400" fill="var(--paper)"/>
    <circle role="img" aria-label="Satisfaction guarantee seal" cx="212" cy="354" r="43" fill="#c9a441"/>
    <circle cx="212" cy="354" r="33" fill="var(--white)"/>
    <polygon points="0,638 528,638 528,750 0,750" fill="var(--sky-light)"/>
    <polygon points="0,646 318,646 318,750 0,750" fill="var(--navy)"/>
    <polygon points="312,640 480,548 528,572 528,750 312,750" fill="var(--navy)"/>
    <polygon role="img" aria-label="Photo: gutter vacuum pole with camera on a roof edge" points="320,645 480,560 528,584 528,750 320,750" fill="url(#poleGrad)"/>
    <defs>
      <linearGradient id="leafGrad" x1="0" y1="0" x2="1" y2="1">
        <stop offset="0" stop-color="#b9c1c6"/><stop offset=".45" stop-color="#b58a3b"/><stop offset="1" stop-color="#7f8a96"/>
      </linearGradient>
      <linearGradient id="poleGrad" x1="0" y1="0" x2="1" y2="1">
        <stop offset="0" stop-color="#6f8f4f"/><stop offset="1" stop-color="#3d4a5e"/>
      </linearGradient>
    </defs>
  </svg>

  <h1 class="abs headline" style="right:22px;top:22px;display:flex;align-items:flex-end;gap:6px">
    <span style="display:block;text-align:left">
      <span class="lg" style="display:block;font-size:28px">Professional</span>
      <span class="md" style="display:block;font-size:25px">Gutter Cleaning</span>
    </span>
    <span class="lg" style="font-size:58px;line-height:.9">Services</span>
  </h1>

  <h2 class="abs offer-title" style="right:20px;top:108px">WHAT WE OFFER</h2>

  <div class="abs brand" style="left:28px;top:330px;font-size:15px"><span class="dot"></span>ClearPane Vista</div>

  <div class="card" style="left:264px;top:165px"><div class="photo" role="img" aria-label="Photo: vacuum hose clearing a gutter" style="background:linear-gradient(160deg,#c8cfc0,#7e5a4b)"></div><div class="label">Gutter cleaning</div></div>
  <div class="card" style="left:393px;top:165px"><div class="photo" role="img" aria-label="Photo: mossy conservatory roof panels" style="background:linear-gradient(160deg,#b9775a,#c9d2cf)"></div><div class="label">Conservatory roof cleaning</div></div>
  <div class="card" style="left:264px;top:333px"><div class="photo" role="img" aria-label="Photo labelling gutter, fascia and soffit" style="background:linear-gradient(160deg,#e6eaee,#8e9aa8)"></div><div class="label">Fascias &amp; Soffits cleaning</div></div>
  <div class="card" style="left:393px;top:333px"><div class="photo" role="img" aria-label="Photo: customer service adviser wearing a headset" style="background:linear-gradient(160deg,#b8c7d6,#d7b69d)"></div><div class="label">Excellent Customer Service</div></div>

  <p class="abs intro" style="left:28px;top:414px">ClearPane Vista offer a fast and easy gutter cleaning service on residential and commercial properties.</p>

  <div class="abs body-copy" style="left:27px;top:507px;width:470px">
    <p>Gutters are an important part of your home. Letting your gutters get blocked up can cause damage to your property, so why not set up an annual plan and make sure you don’t run into problems when winter comes.</p>
    <p style="width:360px">Over time your gutters will fill up with moss, leaves and other unwanted debris which will affect the appearance of your home. When gutters aren’t cleared and emptied on a regular basis they become heavy and risk pulling away from the fascias.</p>
  </div>

  <div class="abs contact" style="left:25px;top:670px">
    <div class="addr">7 Tarnlow Brae, North Pellin Edinburgh EH14 3RW</div>
    <div class="phone"><svg viewBox="0 0 16 20"><path d="M4 1l3 4-2 2c1 3 3 6 5 7l2-2 3 3-2 3C6 17 1 9 2 3z" fill="var(--sky-light)"/></svg>0800 315 4720</div>
    <div class="web">www.clearpane-vista-services.com</div>
  </div>
</section>

</body>
</html>
```